ORB of Quietharbour Business Card Rebrand

Hello Designers! We are looking for help designing our new business card to go in conjunction with our company rebrand. Unfortunately, we have an event mid June that requires we get these printed ASAP (before our new website is launched.) We have a mostly complete Brand Book which I have uploaded to this request for your reference to company information, style, fonts. I've also enclosed our logo file in .eps & .jpg. Attached is a sample business card my boss liked but said was "too simple." I made it in Canva and do not profess to be a designer. NOT FOR DESIGN REFERENCE, ONLY FOR CONTEXT Here is what our old website looks like: https://orbofquietharbour.example/.
Sick
Gathering more feedback
Sick
Sick

```html
<!DOCTYPE html>
<html lang="en">
<head>
<meta charset="utf-8">
<title>ORB of Quietharbour – Business Card</title>
<link href="https://fonts.googleapis.com/css2?family=Roboto+Condensed:wght@400;700&display=swap" rel="stylesheet">
<style>
  :root {
    --bg: #242424;
    --card: #1f2024;
    --card-back: #1c1d21;
    --ink: #ffffff;
    --accent: #4ab3e6;
    --faint: #272c33;
    --emboss: #121316;
    --rule: #9aa0a8;
  }
  * { margin: 0; padding: 0; box-sizing: border-box; }
  html, body { width: 1200px; height: 780px; overflow: hidden; background: var(--bg); }
  body {
    font-family: "Roboto Condensed", Arial, sans-serif;
    color: var(--ink);
    display: flex;
    flex-direction: column;
    align-items: center;
    justify-content: center;
    gap: 30px;
  }
  .card {
    position: relative;
    width: 620px;
    height: 354px;
    overflow: hidden;
  }
  .card--front { background: var(--card); }
  .card--back { background: var(--card-back); display: flex; align-items: center; justify-content: center; }

  .backdrop-circle {
    position: absolute;
    left: 330px; top: 40px;
    width: 260px; height: 260px;
    border-radius: 50%;
    background: var(--faint);
  }
  .brand {
    position: absolute;
    left: 40px; top: 120px;
    display: flex;
    align-items: center;
    gap: 12px;
  }
  .brand__dot {
    width: 34px; height: 34px;
    border-radius: 50%;
    background: var(--accent);
    flex: none;
  }
  .brand__name {
    font-size: 27px;
    font-weight: 700;
    color: var(--ink);
    line-height: 1;
  }
  .divider {
    position: absolute;
    left: 300px; top: 70px;
  }
  .location {
    position: absolute;
    left: 40px; bottom: 34px;
    font-size: 15px;
  }
  .contact {
    position: absolute;
    left: 350px; top: 96px;
  }
  .contact__name {
    font-size: 30px;
    font-weight: 700;
    color: var(--accent);
    line-height: 1.05;
  }
  .contact__title {
    font-size: 14px;
    letter-spacing: 0.5px;
    margin-bottom: 16px;
  }
  .contact__list { list-style: none; }
  .contact__item {
    display: flex;
    align-items: center;
    gap: 9px;
    font-size: 15px;
    margin-bottom: 8px;
  }
  .contact__icon { width: 15px; height: 15px; flex: none; }

  .brand--emboss { position: static; gap: 18px; }
  .brand--emboss .brand__dot { width: 60px; height: 60px; background: var(--emboss); }
  .brand--emboss .brand__name { font-size: 46px; color: var(--emboss); }
</style>
</head>
<body>
  <section class="card card--front" aria-label="Business card front">
    <div class="backdrop-circle"></div>
    <div class="brand">
      <span class="brand__dot"></span>
      <span class="brand__name">ORB of Quietharbour</span>
    </div>
    <svg class="divider" width="40" height="220" viewBox="0 0 40 220" aria-hidden="true">
      <line x1="38" y1="0" x2="2" y2="220" stroke="var(--rule)" stroke-width="1"/>
    </svg>
    <p class="location">Brookmere, GA based (Central Time)</p>
    <div class="contact">
      <h1 class="contact__name">Marten Lisle-Varga</h1>
      <p class="contact__title">MANAGING PARTNER</p>
      <ul class="contact__list">
        <li class="contact__item">
          <svg class="contact__icon" viewBox="0 0 16 16" aria-hidden="true"><path fill="var(--accent)" d="M3.5 1.5l2.5 0 1 3.5-1.7 1.2a8 8 0 0 0 4.5 4.5l1.2-1.7 3.5 1v2.5c0 .8-.7 1.5-1.5 1.5A12 12 0 0 1 2 3c0-.8.7-1.5 1.5-1.5z"/></svg>
          +945-555-0142
        </li>
        <li class="contact__item">
          <svg class="contact__icon" viewBox="0 0 16 16" aria-hidden="true"><circle cx="8" cy="8" r="6.5" fill="none" stroke="var(--accent)" stroke-width="1.6"/><path d="M1.5 8h13M8 1.5c-3 3.5-3 9.5 0 13M8 1.5c3 3.5 3 9.5 0 13" fill="none" stroke="var(--accent)" stroke-width="1.2"/></svg>
          www.orbofquietharbour.example
        </li>
        <li class="contact__item">
          <svg class="contact__icon" viewBox="0 0 16 16" aria-hidden="true"><rect x="1" y="3" width="14" height="10" rx="1" fill="var(--accent)"/><path d="M1.5 3.5L8 9l6.5-5.5" fill="none" stroke="var(--card)" stroke-width="1.3"/></svg>
          marten@orbofquietharbour.example
        </li>
      </ul>
    </div>
  </section>

  <section class="card card--back" aria-label="Business card back">
    <div class="brand brand--emboss">
      <span class="brand__dot"></span>
      <span class="brand__name">ORB of Quietharbour</span>
    </div>
  </section>
</body>
</html>
```